LOGO AND 3 PACKAGES.IN 4 different strengths

I need '3' designs for the packages attached.
Im launching a new electronic cigarette BRAND in Australia.
VORTEK
a logo will be a great advantage also to suit VORTEK...
My company name is Pelmora.
The designs need to be retail orientated and focused on getting the attention of the public in a eye catching way that separates our product from any other.
The designs must have all the information back and front and to the print scale.
Easy to read with a nice layout.
I've included some examples to speed the process up.
Who ever wins this will have the opportunity for a lot more work with me.
The company is looking to expand and grow significantly in the coming year.
We look to be the biggest in our arena.
Website to be - www.vortekvapes.example

Reason: Waiting on final designs and judges its tight.

http://www.regfiles.example/Details/R4471Q00835

For information on packaging design please see this attachment for Lettering and requirements.
I hope this helps.
Nicotine falls into Schedule 7 .
If you want to win other customers over I suggest you know as much as possible .
If your not interested then no worries.

You have until today to wrap it up people thanks.

Lyle

Target Market(s)

SMOKERS
PEOPLE LOOKING TO QUIT
Convenience stores major and minor

Industry/Entity Type

Electronic

Logo Text

VORTEK

Logo styles of interest
Emblem Logo
Pictorial/Combination Logo
Abstract Logo
Character Logo
Wordmark Logo
Font styles to use
Sans Serif
Decorative
Other font styles liked:
• VORTEK or CUSTOM TEXT to SUIT

Colors
00a98f
33a7d7
fbee3e
ec1f27
e34197
f37123

Requirements
Must have
• THE ALTERNATIVE SMOKING DEVICE
THE MOST TRUSTED BRAND
THE DISPOSABLE pack and the Rechargeable cartomisers 1 cartomizer = 2packs of cigarettes
400 puffs
VORTEK IS AN AUSTRALIAN BRAND
MUST BE +18
REFF TO EXAMPLES FOR OTHER MUST HAVES PRODUCT CERTIFICATION
SGS ROHS ECT..
Each package has a different strength of nicotine zero%-1.8%-and 2.4%
In 4 different flavors menthol-special blend Tobacco-New Vanilla-and Coffee/Mocha
For now.
Nice to have
• UV silver, green's blue's and reds
I like the carbon look and the metal grating backgrounds.
Slogan
"LIVE FOR IT"
QUALITY BRAND 100% GUARANTEED
Should not have
• NOTHING IMPLYING THAT THIS IS A HEALTHIER OPTION THEN SMOKING
ANY other types of packages PLEASE stick to the templates
WORD Disposable, WORD REchargeable and WORD CArtomizers.

```html
<!DOCTYPE html>
<html lang="en">
<head>
<meta charset="utf-8">
<title>VORTEK Mocha Coffee Pack</title>
<link rel="stylesheet" href="https://fonts.googleapis.com/css2?family=Lilita+One&family=Exo+2:ital,wght@0,800;1,700;1,800&family=Montserrat:ital,wght@0,400;0,600;1,600&family=Oswald:wght@600&display=swap">
<style>
:root{
  --page:#eaf3f9;
  --navy:#132553;
  --navy-deep:#0c1a40;
  --white:#ffffff;
  --chrome:#c5dcf2;
  --sky:#33a7d7;
  --orange:#f37123;
  --orange-light:#f9a436;
  --red:#ec1f27;
  --gold:#f2b02a;
  --line:#d6e2ef;
  --tan:#f0b36a;
}
*{box-sizing:border-box;margin:0;padding:0}
html,body{width:1200px;height:1016px;overflow:hidden;background:var(--page)}
body{position:relative;font-family:"Montserrat",sans-serif;color:var(--white)}
.panel{position:absolute;top:75px;width:588px;height:840px;border-radius:30px;overflow:hidden;
  background:linear-gradient(180deg,var(--navy) 0%,var(--navy-deep) 100%);border:3px solid var(--navy-deep)}
.panel--front{left:5px}
.panel--back{left:611px;box-shadow:inset 0 0 0 5px var(--navy),inset 0 0 0 7px var(--white)}
.abs{position:absolute}
.guides{position:absolute;left:0;top:0}
/* front */
.seal{left:20px;top:20px;width:135px;height:135px;border-radius:50%;
  background:radial-gradient(circle,var(--gold) 0 55%,#fff3c9 56% 60%,var(--gold) 61%);}
.warning{left:435px;top:22px;width:131px;height:55px;background:var(--white);border:3px solid var(--red);
  color:#111;text-align:center;font-family:"Montserrat",sans-serif;font-weight:600;line-height:1}
.warning b{display:block;font-size:22px;margin-top:5px;font-weight:600}
.warning span{display:block;font-size:14px;margin-top:4px}
.directions{left:40px;top:168px;width:380px;text-align:center;font-size:13px;line-height:13px}
.directions h3{font-size:12.5px;font-style:italic;font-weight:600;margin-bottom:16px}
.directions p{margin-bottom:12px}
.directions .note{font-weight:600;font-size:12.5px;margin-top:2px}
.use-pill{left:202px;top:348px;width:188px;height:55px;border-radius:14px;
  background:linear-gradient(180deg,var(--orange-light),var(--orange));border:2px solid #fff;
  font-family:"Exo 2",sans-serif;font-style:italic;font-weight:700;font-size:18px;color:#fff;
  display:flex;align-items:center;justify-content:center}
.use{width:150px;text-align:center;top:425px}
.use svg{display:block;margin:0 auto}
.use-label{font-family:"Exo 2",sans-serif;font-style:italic;font-weight:800;font-size:27px;line-height:25px;margin-top:6px}
.brand{font-family:"Exo 2",sans-serif;font-weight:800;color:var(--chrome);letter-spacing:2px;line-height:1}
.brand--front{left:55px;top:595px;font-size:96px}
.tagline{font-family:"Oswald",sans-serif;font-weight:600;color:var(--orange);font-size:19px;letter-spacing:-.3px;line-height:1;white-space:nowrap}
.tagline--front{left:193px;top:692px}
.side-claim{left:520px;top:706px;transform:rotate(-90deg);transform-origin:0 0;white-space:nowrap;
  font-family:"Montserrat",sans-serif;font-weight:600;font-size:20px;letter-spacing:.6px}
.cert-band{left:0;bottom:0;width:100%;height:116px;background:var(--white);display:flex;align-items:center;gap:22px;padding-left:40px}
.cert{width:60px;height:48px;border-radius:8px;background:#d9dde3}
.cert--round{width:52px;border-radius:50%;background:#f3a35f}
.cert--diamond{width:40px;height:40px;border-radius:3px;transform:rotate(45deg);background:none;border:3px solid var(--red);margin:0 6px}
.cert--green{width:48px;border-radius:50%;background:#9ed9b3}
.cert--plain{width:40px;background:#c9cdd3}
/* back */
.top-line{left:0;top:8px;width:100%;text-align:center;font-family:"Exo 2",sans-serif;font-style:italic;font-weight:800;font-size:24px;padding-left:30px}
.top-line small{font-size:11px;vertical-align:8px}
.guarantee{left:17px;top:20px;width:132px;height:132px;border-radius:50%;
  background:radial-gradient(circle,var(--red) 0 55%,#fff 56% 60%,var(--red) 61% 80%,var(--gold) 81%)}
.flavor{left:252px;top:111px;width:140px;font-family:"Lilita One",sans-serif;font-size:38px;line-height:33px;color:var(--tan);text-align:center;letter-spacing:.5px}
.photo{left:414px;top:62px;width:158px;height:158px;border-radius:50%;border:4px solid var(--sky);
  background:radial-gradient(circle at 45% 40%,#f1e6d8 0 30%,#9c6b45 45%,#6a5a52 75%,#3d3330)}
.slogan{left:32px;top:508px;transform:rotate(-90deg);transform-origin:0 0;white-space:nowrap;
  font-family:"Exo 2",sans-serif;font-style:italic;font-weight:800;font-size:24px;color:var(--sky)}
.brand--back{left:175px;top:216px;font-size:92px}
.tagline--back{left:290px;top:305px}
.age{left:36px;top:774px;width:92px;height:46px;background:var(--white);border:3px solid var(--red);
  display:flex;align-items:center;gap:4px;padding-left:7px}
.age b{background:#111;color:#fff;font-size:13px;padding:6px 4px;font-weight:600}
.nicotine{left:202px;top:776px;font-size:18px}
</style>
</head>
<body>

<section class="panel panel--front">
  <svg class="guides" width="588" height="840" viewBox="0 0 588 840" aria-hidden="true">
    <path d="M190 75 H250 Q260 45 282 43 Q304 45 314 75 H400 Q412 77 412 92 Q412 107 400 109 H185 Q172 107 172 92 Q172 77 190 75Z" fill="none" stroke="var(--line)" stroke-width="2"/>
    <path d="M425 165 H422 M425 165 V325 H42" fill="none" stroke="var(--red)" stroke-width="1.5" stroke-dasharray="16 10"/>
    <path d="M510 165 V725" fill="none" stroke="var(--red)" stroke-width="1.5" stroke-dasharray="16 10"/>
    <path d="M42 330 V725 M42 330 Q42 326 50 326" fill="none" stroke="var(--line)" stroke-width="1.5" stroke-dasharray="16 10"/>
  </svg>
  <div class="abs seal" role="img" aria-label="Premium quality seal"></div>
  <div class="abs warning"><b>WARNING</b><span>ADULTS ONLY</span></div>
  <div class="abs directions">
    <h3>DIRECTIONS FOR USE:</h3>
    <p>Screw the cartridge into the battery. VORTEK will automatically activate as you take a puff.</p>
    <p>You will see the tip light up. When the tip starts to flash, the battery &amp; cartridge are nearly empty and should be replaced.</p>
    <p class="note">PLEASE READ FULL INSTRUCTIONS INSIDE</p>
  </div>
  <div class="abs use-pill">Perfect for use in:</div>

  <div class="abs use" style="left:67px">
    <svg width="88" height="88" viewBox="0 0 88 88" aria-hidden="true"><circle cx="44" cy="44" r="41" fill="var(--sky)" stroke="#fff" stroke-width="3"/><path d="M22 44 L44 24 L66 44 H60 V66 H28 V44Z" fill="#fff"/><rect x="39" y="52" width="10" height="14" fill="var(--sky)"/></svg>
    <div class="use-label">Home</div>
  </div>
  <div class="abs use" style="left:217px">
    <svg width="88" height="88" viewBox="0 0 88 88" aria-hidden="true"><circle cx="44" cy="44" r="41" fill="var(--sky)" stroke="#fff" stroke-width="3"/><path d="M14 46 Q40 36 74 40 Q80 42 74 46 L40 52Z M38 40 L52 22 L58 24 L52 40Z M40 50 L56 66 L62 64 L54 48Z" fill="#fff"/></svg>
    <div class="use-label">Air<br>Travel</div>
  </div>
  <div class="abs use" style="left:368px">
    <svg width="88" height="88" viewBox="0 0 88 88" aria-hidden="true"><circle cx="44" cy="44" r="41" fill="var(--sky)" stroke="#fff" stroke-width="3"/><path d="M22 60 V46 L28 32 H60 L66 46 V60Z" fill="#fff"/><rect x="31" y="36" width="26" height="9" fill="var(--sky)"/><circle cx="30" cy="52" r="3" fill="var(--sky)"/><circle cx="58" cy="52" r="3" fill="var(--sky)"/></svg>
    <div class="use-label">Car</div>
  </div>

  <div class="abs brand brand--front">VORTEK</div>
  <div class="abs tagline tagline--front">THE ALTERNATIVE SMOKING DEVICE</div>
  <div class="abs side-claim">EQUALS 2 PACKS OF CIGARETTES - 400 PUFFS</div>

  <div class="abs cert-band">
    <div class="cert" role="img" aria-label="Compliance certificate mark"></div>
    <div class="cert cert--round" role="img" aria-label="Manufacturing certificate mark"></div>
    <div class="cert cert--diamond" role="img" aria-label="Hazard symbol"></div>
    <div class="cert cert--green" role="img" aria-label="Recycling mark"></div>
    <div class="cert cert--plain" role="img" aria-label="Conformity mark"></div>
  </div>
</section>

<section class="panel panel--back">
  <svg class="guides" width="588" height="840" viewBox="0 0 588 840" aria-hidden="true">
    <path d="M190 75 H250 Q260 45 282 43 Q304 45 314 75 H400 Q412 77 412 92 Q412 107 400 109 H185 Q172 107 172 92 Q172 77 190 75Z" fill="none" stroke="var(--line)" stroke-width="2"/>
    <rect x="74" y="165" width="86" height="595" rx="12" fill="none" stroke="var(--line)" stroke-width="2"/>
    <rect x="188" y="325" width="355" height="95" rx="12" fill="none" stroke="var(--line)" stroke-width="2"/>
    <rect x="188" y="465" width="355" height="97" rx="12" fill="none" stroke="var(--line)" stroke-width="2"/>
    <path d="M225 608 H535 Q545 608 545 618 V730 Q545 740 535 740 H225 Q215 740 215 730 V710 H198 V638 H215 V618 Q215 608 225 608Z" fill="none" stroke="var(--line)" stroke-width="2"/>
  </svg>
  <div class="abs top-line"><small>THE </small>MOST TRUSTED BRAND</div>
  <div class="abs guarantee" role="img" aria-label="Quality guarantee seal"></div>
  <div class="abs photo" role="img" aria-label="Cup of mocha coffee with cinnamon and star anise"></div>
  <div class="abs flavor">Mocha<br>Coffee<br>Flavor</div>
  <div class="abs brand brand--back">VORTEK</div>
  <div class="abs tagline tagline--back">THE ALTERNATIVE SMOKING DEVICE</div>
  <div class="abs slogan">"LIVE FOR IT"</div>
  <div class="abs age"><b>18+</b>
    <svg width="44" height="24" viewBox="0 0 44 24" aria-hidden="true"><path d="M2 8 H24 M10 8 V20 H30 Q36 20 36 14 V8 H28" fill="none" stroke="#111" stroke-width="2"/><rect x="38" y="6" width="4" height="14" fill="var(--red)"/></svg>
  </div>
  <div class="abs nicotine">1.8% nicotine by volume</div>
</section>

</body>
</html>
```